Coupon/promo code site

I am looking for a one page website that will provide a list of coupon codes that are used at checkout when buying something online. The site will only have coupon codes for one online retailer. I would like this to be generic (i.e. not specific to any one retailer). I would like to have some interchangeable parts so that I could later customize the site so that it is specific to any given retailer.

I envision the site having a list of coupon codes with information about each code like when it expires and what it provides. For example there would be a: code, expiration date, short description or name, and a longer description (i.e. details).
Updates

Project Deadline Extended
Reason: I am going to submit a wire frame that provides a better idea of what I am looking for.

I have uploaded a wire frame that gives a more clear indication of what I am looking for.  Please see this before submitting designs.  If you have already submitted a design, please revise your design considering the wire frame I have provided.

Thanks,
Derek

Target Market(s)

Someone who is shopping online and searching for a specific retailers coupon codes

Industry/Entity Type

Coupon

Requirements
Must have
• I would like the site to have a white or light colored background.

I need a place or two where I can interchangeably place different retailers' logos.

The web page should have a title like, "[retailer's] online coupon code"

In addition to a list or table of coupon codes, there should below this be a list or table of special offers or sale items.

At the very bottom in a way that is not too noticeable, it should say, "This coupon site was created by PLV Deals."

There should be a section (probably on the right side) that allows a user to submit their email address to be notified in the future of specials/deals for this retailer.

There should be a nice looking link that goes to the online retailer's website.
Nice to have
• Example sites with a look and feel that I like are:

http://www.halvorpine.com/
https://thebramlet.com/
http://www.artvinhub.com

This is an example of a site with coupon codes for just one retailer. This site is a little too busy, but you get the idea:
www.makeoplank.com/coupon-codes‎

```html
<!DOCTYPE html>
<html lang="en">
<head>
<meta charset="utf-8">
<title>[Retailer's] Online Coupon Code</title>
<link rel="stylesheet" href="https://fonts.googleapis.com/css2?family=Ubuntu:wght@300;400;500;700&display=swap">
<style>
:root{
  --nav-blue:#2d68b9;
  --band-blue:#3a86dd;
  --accent-blue:#4a9be8;
  --deep-blue:#1f4f8f;
  --orange:#f2572f;
  --page:#f0f0f0;
  --white:#ffffff;
  --line:#dcdcdc;
  --ink:#2b2b2b;
  --body:#7a7a7a;
  --muted:#b0b0b0;
  --field:#e9e9e9;
  --grey-btn:#8d8d8d;
  --foot:#3b3b3b;
  --foot-bar:#2f2f2f;
  --foot-text:#a9a9a9;
}
*{box-sizing:border-box;margin:0;padding:0}
html,body{width:1200px;height:2321px;overflow:hidden}
body{position:relative;background:var(--page);font-family:'Ubuntu',sans-serif;color:var(--ink)}
.abs{position:absolute}
.btn{position:absolute;display:flex;align-items:center;justify-content:center;font-weight:500;font-size:13px;color:var(--white);letter-spacing:.5px;border-radius:3px}

/* header */
.site-nav{left:0;top:0;width:1200px;height:77px;background:var(--nav-blue)}
.brand{left:130px;top:26px;font-size:20px;font-weight:700;color:var(--white)}
.nav-links{left:420px;top:31px;display:flex;gap:44px;font-size:12px;color:#dbe7f7}
.join{left:889px;top:23px;width:91px;height:28px;background:var(--accent-blue);font-size:12px}
.login{left:991px;top:23px;width:79px;height:28px;background:var(--deep-blue);font-size:12px;border:1px solid #3f72b6}
.title-band{left:0;top:77px;width:1200px;height:97px;background:var(--band-blue);display:flex;align-items:center;justify-content:center;color:var(--white);font-size:38px;font-weight:300;letter-spacing:.5px}
.search-band{left:0;top:174px;width:1200px;height:98px;background:var(--white);border-bottom:1px solid var(--line)}
.search-field{left:130px;top:202px;width:617px;height:44px;background:var(--field);border:1px solid #d4d4d4;border-radius:3px;font-size:13px;color:var(--muted);display:flex;align-items:center;padding-left:42px}
.search-btn{left:770px;top:202px;width:110px;height:44px;background:var(--orange)}
.browse-btn{left:930px;top:202px;width:140px;height:44px;background:var(--grey-btn)}

/* company card */
.company-card{left:130px;top:332px;width:940px;height:404px;background:var(--white);border:1px solid var(--line)}
.logo-text{font-size:17px;font-weight:700;color:var(--ink);text-align:center}
.company-desc{left:364px;top:356px;width:375px}
.company-desc h3{font-size:16px;font-weight:500;margin-bottom:10px}
.company-desc p{font-size:12.5px;line-height:20px;color:var(--body);margin-bottom:18px}
.visit-btn{left:364px;top:592px;width:140px;height:37px;background:var(--accent-blue);font-size:12px}
.stats-panel{left:757px;top:332px;width:313px;height:404px;border-left:1px solid var(--line)}
.stats-head{left:757px;top:332px;width:313px;height:88px;background:#f4f4f4;border-bottom:1px solid var(--line)}
.photo{position:absolute;width:114px;height:114px}

/* coupons */
.list-head{left:130px;top:777px;font-size:14px;font-weight:500;color:var(--muted);letter-spacing:.5px}
.list-head b{color:var(--accent-blue);font-weight:700}
.sort{left:716px;top:779px;font-size:11px;color:var(--muted)}
.sort span{color:var(--accent-blue)}
.coupon{position:absolute;left:130px;width:699px;height:154px;background:var(--white);border:1px solid var(--line);border-radius:3px}
.coupon .thumb{position:absolute;left:23px;top:24px;width:200px;height:104px}
.coupon .info{position:absolute;left:246px;top:24px;width:270px}
.coupon h4{font-size:15px;font-weight:500;margin-bottom:12px}
.coupon p{font-size:12px;line-height:20px;color:var(--body)}
.coupon .deal{position:absolute;left:531px;top:0;width:167px;height:152px;border-left:1px solid var(--line);text-align:center}
.deal .amt{margin-top:26px;font-size:18px;font-weight:700;color:var(--orange)}
.deal .left{font-size:11px;color:var(--muted);margin-top:2px}
.deal .act{position:absolute;left:20px;top:90px;width:128px;height:36px;display:flex;align-items:center;justify-content:center;font-size:12px;font-weight:500;border-radius:3px;color:var(--white)}

/* sidebar */
.side{left:850px;width:220px}
.side h3{font-size:16px;font-weight:500;margin-bottom:10px}
.side p{font-size:12.5px;line-height:21px;color:var(--body)}
.video{left:850px;top:991px;width:220px;height:199px;background:#000}
.quote{left:850px;top:1209px;width:220px;height:153px;background:var(--white);border:1px solid var(--line);border-radius:3px;padding:15px;font-size:12px;line-height:21px;color:var(--body)}
.quote-name{left:850px;top:1390px;width:220px;text-align:right;font-size:12px;font-weight:700}

/* pagination */
.page{position:absolute;top:1509px;height:46px;background:var(--white);border:1px solid var(--line);border-radius:3px;display:flex;align-items:center;justify-content:center;font-size:14px;font-weight:500}
.page.on{background:var(--orange);border-color:var(--orange);color:var(--white)}

/* newsletter */
.news-band{left:0;top:1618px;width:1200px;height:97px;background:var(--white);border-top:1px solid var(--line);border-bottom:1px solid var(--line)}
.news-label{left:130px;top:1657px;font-size:15px;font-weight:700}
.field{position:absolute;top:1643px;height:45px;background:var(--field);border:1px solid #d4d4d4;border-radius:3px;font-size:13px;color:var(--muted);display:flex;align-items:center;padding-left:18px}
.subscribe{left:928px;top:1643px;width:142px;height:45px;background:var(--orange)}

/* popular */
.pop-head{left:130px;top:1779px;font-size:15px;font-weight:500;color:#888;letter-spacing:.5px}
.pop-card{position:absolute;top:1815px;width:111px;height:111px;background:var(--white);border:1px solid var(--line);border-radius:3px;padding:10px}
.pop-card div{width:89px;height:89px}
.arrow{position:absolute;top:1855px}

/* footer */
.footer{left:0;top:1991px;width:1200px;height:260px;background:var(--foot)}
.foot-col{position:absolute;top:2032px;color:var(--foot-text);font-size:12px;line-height:22px}
.foot-col h5{font-size:14px;font-weight:700;color:var(--white);margin-bottom:10px}
.menu li{list-style:none}
.footer-bar{left:0;top:2251px;width:1200px;height:70px;background:var(--foot-bar)}
.foot-brand{left:130px;top:2274px;font-size:20px;font-weight:700;color:var(--white)}
.copy{left:414px;top:2280px;font-size:12px;color:var(--foot-text)}
.social{position:absolute;top:2268px;width:32px;height:32px;border-radius:50%;background:#6d6d6d}
</style>
</head>
<body>

<header>
  <div class="abs site-nav"></div>
  <div class="abs brand">WEBSITE NAME</div>
  <nav class="abs nav-links"><span>HOME</span><span>BLOG</span><span>EXTRA</span><span>COUPONS</span><span>POST</span></nav>
  <div class="btn join">+ JOIN US</div>
  <div class="btn login">LOG IN</div>
  <h1 class="abs title-band">[RETAILER'S] ONLINE COUPON CODE</h1>
  <div class="abs search-band"></div>
  <div class="abs search-field">Search listing</div>
  <svg class="abs" style="left:145px;top:216px" width="16" height="16" viewBox="0 0 16 16"><circle cx="6.5" cy="6.5" r="5" fill="none" stroke="#9a9a9a" stroke-width="1.6"/><line x1="10.5" y1="10.5" x2="14.5" y2="14.5" stroke="#9a9a9a" stroke-width="1.6"/></svg>
  <svg class="abs" style="left:715px;top:216px" width="16" height="16" viewBox="0 0 16 16"><circle cx="8" cy="8" r="7" fill="none" stroke="#9a9a9a" stroke-width="1.4"/><path d="M5 5l6 6M11 5l-6 6" stroke="#9a9a9a" stroke-width="1.4"/></svg>
  <div class="btn search-btn">SEARCH</div>
  <div class="btn browse-btn" style="justify-content:flex-start;padding-left:28px">BROWSE</div>
  <svg class="abs" style="left:1040px;top:216px" width="10" height="16" viewBox="0 0 10 16"><path d="M1 6l4-4 4 4M1 10l4 4 4-4" fill="none" stroke="#fff" stroke-width="1.5"/></svg>
</header>

<section class="company">
  <div class="abs company-card"></div>
  <div class="abs logo-text" style="left:130px;top:395px;width:234px">RETAILER'S LOGO</div>
  <div class="abs company-desc">
    <h3>Company Description</h3>
    <p>Lorem ipsum dolor sit amet, consectetur adipisicing elit. Architecto maiores possimus assumenda velit itaque cumque sint explicabo hic incidunt et in repellendus optio obcaecati rerum ipsam quia repudiandae illum suscipit?</p>
    <p>Lorem ipsum dolor sit amet, consectetur adipisicing elit. Aperiam adipisci quod tempora fugiat officiis ducimus nam incidunt illum aspernatur. Libero iste laboriosam tenetur suscipit non rerum eum totam accusamus magni!</p>
  </div>
  <div class="btn visit-btn">VISIT WEBSITE</div>
  <div class="abs stats-panel"></div>
  <div class="abs stats-head"></div>
  <div class="abs" style="left:775px;top:368px;font-size:13px;font-weight:700">TOTAL COUPONS</div>
  <div class="abs" style="left:960px;top:350px;width:60px;text-align:center;font-size:28px;font-weight:500">15</div>
  <div class="abs" style="left:960px;top:386px;width:60px;text-align:center;font-size:11px;color:var(--muted)">coupons</div>
  <div class="photo" style="left:789px;top:453px;background:linear-gradient(#5d86b8,#8a5a48)" role="img" aria-label="Photo of a pagoda-style city gate"></div>
  <div class="photo" style="left:924px;top:453px;background:linear-gradient(#7fa6d6,#8f8a80)" role="img" aria-label="Photo of city skyscrapers"></div>
  <div class="photo" style="left:789px;top:587px;background:linear-gradient(135deg,#2e2a1c,#c7923a 55%,#3a6b2b)" role="img" aria-label="Photo of a lit night street scene"></div>
  <div class="photo" style="left:924px;top:587px;background:linear-gradient(#1f3f7a,#b38a3a)" role="img" aria-label="Photo of a domed monument at dusk"></div>
</section>

<section class="coupons">
  <div class="abs list-head">COUPONS BY <b>COMPANY</b> - 2453 RESULTS</div>
  <div class="abs sort">Popular &nbsp;|&nbsp; <span>Newest</span></div>

  <article class="coupon" style="top:805px">
    <div class="logo-text" style="position:absolute;left:23px;top:65px;width:200px">RETAILER'S LOGO</div>
    <div class="info"><h4>Product Title + Additional Info</h4><p>Etiam ultrices vestibulum pulvinar. Pellentesque feugiat ultricies pulvinar. Fusce mattis rhoncus justo at gravida.</p></div>
    <div class="deal"><div class="amt">$30 OFF</div><div class="left">14 days left</div><div class="act" style="background:var(--orange)">SHOW COUPON</div></div>
  </article>

  <article class="coupon" style="top:982px">
    <div class="thumb" style="background:linear-gradient(135deg,#3a2c22,#8a6a4a 50%,#2a2a2a)" role="img" aria-label="Photo of headphones on a keyboard"></div>
    <div class="info"><h4>Product Title + Additional Info</h4><p>Etiam ultrices vestibulum pulvinar. Pellentesque feugiat ultricies pulvinar. Fusce mattis rhoncus justo at gravida.</p></div>
    <div class="deal"><div class="amt">$30 OFF</div><div class="left">14 days left</div><div class="act" style="background:var(--accent-blue)">LEARN MORE</div></div>
  </article>

  <article class="coupon" style="top:1158px">
    <div class="thumb" style="background:linear-gradient(135deg,#e9e4da,#c98a5a 55%,#f1ece4)" role="img" aria-label="Photo of sushi rolls on a plate"></div>
    <div class="info"><h4>Product Title + Additional Info</h4><p>Etiam ultrices vestibulum pulvinar. Pellentesque feugiat ultricies pulvinar. Fusce mattis rhoncus justo at gravida.</p></div>
    <div class="deal"><div class="amt">10% OFF</div><div class="left">5 days left</div><div class="act" style="background:#ececec;border:1px solid #cfcfcf;color:#666">SGSA29O</div></div>
  </article>

  <article class="coupon" style="top:1335px">
    <div class="thumb" style="background:linear-gradient(135deg,#4a2f22,#c79a6a 50%,#2b1d16)" role="img" aria-label="Photo of a close-up mechanical part"></div>
    <div class="info"><h4>Product Title + Additional Info</h4><p>Etiam ultrices vestibulum pulvinar. Pellentesque feugiat ultricies pulvinar. Fusce mattis rhoncus justo at gravida.</p></div>
    <div class="deal"><div class="amt">10% OFF</div><div class="left">5 days left</div><div class="act" style="background:#dcecfb;border:2px solid var(--accent-blue);color:var(--accent-blue)">SGSA29O</div></div>
  </article>

  <div class="page" style="left:130px;width:109px">Previous</div>
  <div class="page" style="left:253px;width:46px">1</div>
  <div class="page on" style="left:311px;width:49px">2</div>
  <div class="page" style="left:371px;width:49px">3</div>
  <div class="page" style="left:432px;width:48px">4</div>
  <div class="page" style="left:492px;width:49px">5</div>
  <div class="page" style="left:555px;width:76px">Next</div>
</section>

<aside>
  <div class="abs side" style="top:805px">
    <h3>How It Works?</h3>
    <p>Donec suscipit ipsum pulvinar arcu dapibus fermentum. Nam dignissim lobortis justo, vel volutpat mi mattis eu. Integer ut erat purus. Praesent erat massa, tincidunt ac vestibulum ac.</p>
  </div>
  <div class="abs video" role="img" aria-label="Video player"></div>
  <div class="abs quote">New Styles On Just Reduced Merchandise! Save On Hundreds Of Just Reduced Items And Sign Up With Us! New Styles On Just Reduced Merchandise!</div>
  <div class="abs quote-name">Nate Corwin</div>
</aside>

<section class="newsletter">
  <div class="abs news-band"></div>
  <div class="abs news-label">NEWSLETTER SIGNUP</div>
  <div class="field" style="left:371px;width:219px">Enter Your Name</div>
  <div class="field" style="left:610px;width:295px">Enter Your E-mail</div>
  <div class="btn subscribe">SUBSCRIBE</div>
</section>

<section class="popular">
  <div class="abs pop-head">POPULAR COMPANIES</div>
  <svg class="arrow" style="left:86px" width="14" height="24" viewBox="0 0 14 24"><path d="M12 2L3 12l9 10" fill="none" stroke="#999" stroke-width="2"/></svg>
  <div class="pop-card" style="left:130px"><div style="background:linear-gradient(#5d86b8,#8a5a48)" role="img" aria-label="Company photo"></div></div>
  <div class="pop-card" style="left:267px"><div style="background:linear-gradient(#7fa6d6,#8f8a80)" role="img" aria-label="Company photo"></div></div>
  <div class="pop-card" style="left:404px"><div style="background:linear-gradient(135deg,#2e2a1c,#c7923a 55%,#3a6b2b)" role="img" aria-label="Company photo"></div></div>
  <div class="pop-card" style="left:541px"><div style="background:linear-gradient(#1f3f7a,#b38a3a)" role="img" aria-label="Company photo"></div></div>
  <div class="pop-card" style="left:678px"><div style="background:linear-gradient(#5d86b8,#8a5a48)" role="img" aria-label="Company photo"></div></div>
  <div class="pop-card" style="left:815px"><div style="background:linear-gradient(#7fa6d6,#8f8a80)" role="img" aria-label="Company photo"></div></div>
  <div class="pop-card" style="left:952px"><div style="background:linear-gradient(135deg,#2e2a1c,#c7923a 55%,#3a6b2b)" role="img" aria-label="Company photo"></div></div>
  <svg class="arrow" style="left:1100px" width="14" height="24" viewBox="0 0 14 24"><path d="M2 2l9 10-9 10" fill="none" stroke="#999" stroke-width="2"/></svg>
</section>

<footer>
  <div class="abs footer"></div>
  <div class="foot-col" style="left:130px;width:300px">
    <h5>ABOUT</h5>
    <p>Ut sodales ultrices metus, at molestie tellus cursus quis. Cras placerat bibendum quam sed facilisis. Suspendisse dapibus eros eget tellus tempor lacinia. Cras ornare lorem sit amet arcu accumsan ut tristique est fringilla.</p>
  </div>
  <div class="foot-col" style="left:529px;width:320px">
    <h5>RECENT TWEETS</h5>
    <p style="padding-left:22px;position:relative"><span style="position:absolute;left:0;top:7px;width:10px;height:10px;border-radius:50%;background:#777"></span>This coupon site is awesome! @hollowreed<br><span style="color:#777;font-size:11px">posted 5 minutes ago</span></p>
  </div>
  <div class="foot-col menu" style="left:928px">
    <h5>MENU</h5>
    <ul><li>› Home</li><li>› About</li><li>› Terms &amp; Conditions</li><li>› Privacy Policy</li><li>› Jobs</li></ul>
  </div>
  <div class="abs footer-bar"></div>
  <div class="abs foot-brand">WEBSITE NAME</div>
  <div class="abs copy">Copyright © 2013, This coupon site was created by PLV Deals.</div>
  <div class="social" style="left:961px" aria-label="Social link"></div>
  <div class="social" style="left:998px" aria-label="Social link"></div>
  <div class="social" style="left:1035px" aria-label="Social link"></div>
</footer>

</body>
</html>
```